Business Card Design

Professional solutions in (servers, security, networks, programming)

Industry/Entity Type

Business

Contact Information for Business Card

Nadim Fouzan
Internet services and network solutions
TDK - GLPW - GLPT
netdesk@kavo-lin.com / 05291473806
www.kavo-lin.com

```html
<!DOCTYPE html>
<html lang="en">
<head>
<meta charset="utf-8">
<title>Kavolin Co — Business Card</title>
<link rel="stylesheet" href="https://fonts.googleapis.com/css2?family=Montserrat:wght@300;500;700&family=Open+Sans:wght@300;400&display=swap">
<style>
  :root {
    --stage: #e7e3dc;
    --card: #0f3b4f;
    --card-deep: #0b2f40;
    --ink: #ffffff;
    --ink-soft: #a9bcc6;
    --rule: #8aa3af;
  }
  * { box-sizing: border-box; margin: 0; padding: 0; }
  html, body {
    width: 1200px; height: 1022px; overflow: hidden;
    background: var(--stage);
  }
  .stage {
    width: 1200px; height: 1022px;
    display: flex; align-items: center; justify-content: center;
  }
  .card {
    position: relative;
    width: 900px; height: 514px;
    border-radius: 26px;
    background: linear-gradient(135deg, var(--card) 0%, var(--card-deep) 100%);
    box-shadow: 0 18px 40px rgba(0,0,0,0.25);
    color: var(--ink);
  }
  .brand {
    position: absolute; left: 150px; top: 120px;
    display: flex; align-items: center; gap: 22px;
  }
  .brand-dot {
    width: 26px; height: 26px; border-radius: 50%;
    background: var(--ink);
  }
  .brand-name {
    font-family: "Montserrat", sans-serif;
    font-weight: 500; font-size: 64px; letter-spacing: 2px;
    text-transform: uppercase; line-height: 1;
  }
  .tagline {
    position: absolute; left: 150px; top: 202px;
    font-family: "Open Sans", sans-serif; font-weight: 300;
    font-size: 21px; letter-spacing: 0.5px;
    text-transform: uppercase; color: var(--ink-soft);
  }
  .rule {
    position: absolute; left: 190px; top: 248px;
    width: 540px; height: 1.5px; background: var(--rule);
  }
  .person {
    position: absolute; left: 150px; top: 272px;
  }
  .person-name {
    font-family: "Montserrat", sans-serif; font-weight: 700;
    font-size: 30px; letter-spacing: 1px; text-transform: uppercase;
  }
  .person-creds {
    margin-top: 6px; margin-left: 60px;
    font-family: "Open Sans", sans-serif; font-weight: 300;
    font-size: 19px; color: var(--ink-soft);
  }
  .contact {
    position: absolute; left: 500px; top: 272px;
    list-style: none;
    font-family: "Open Sans", sans-serif; font-weight: 400;
    font-size: 21px; line-height: 1.55;
  }
  .contact li { display: flex; align-items: center; gap: 12px; }
  .contact svg { width: 14px; height: 14px; fill: none; stroke: var(--ink); stroke-width: 1.6; }
</style>
</head>
<body>
  <main class="stage">
    <section class="card" aria-label="Kavolin Co business card">
      <div class="brand">
        <span class="brand-dot"></span>
        <span class="brand-name">Kavolin Co</span>
      </div>
      <p class="tagline">Internet services and network solutions</p>
      <div class="rule"></div>
      <div class="person">
        <p class="person-name">Nadim Fouzan</p>
        <p class="person-creds">TDK - GLPW - GLPT</p>
      </div>
      <ul class="contact">
        <li>
          <svg viewBox="0 0 16 16"><path d="M4 1.5l2.5 3-1.5 2c1 2 2.5 3.5 4.5 4.5l2-1.5 3 2.5-1.5 2.5C7 15 1 9 1.5 3z"/></svg>
          <span>05291473806</span>
        </li>
        <li>
          <svg viewBox="0 0 16 16"><rect x="1.5" y="3.5" width="13" height="9"/><path d="M1.5 3.5L8 9l6.5-5.5"/></svg>
          <span>netdesk@kavo-lin.com</span>
        </li>
        <li>
          <svg viewBox="0 0 16 16"><circle cx="8" cy="8" r="6.5"/><path d="M1.5 8h13M8 1.5c-3 3.5-3 9.5 0 13M8 1.5c3 3.5 3 9.5 0 13"/></svg>
          <span>www.kavo-lin.com</span>
        </li>
      </ul>
    </section>
  </main>
</body>
</html>
```